terras letterhead

We would like to create a new letterhead that our company will use for proposals, invoices, statements and letters. Our company name is Terra-Vantage. We are a landscape design/build and landscape maintenance company. We have a web site Terra-Vantage.example where our logo (the leaf with the lettering within it only) is displayed.

Industry/Entity Type

Graphic Design

Requirements
Must have
• Address and info on our current letterhead (uploaded)
Nice to have
• We would like the design to look presentable in grey scale as well as color.
Should not have
• Do not want to infringe much on the normal useable area within the normal print areas.

```html
<!DOCTYPE html>
<html lang="en">
<head>
<meta charset="utf-8">
<title>Terra-Vantage Letterhead</title>
<link rel="stylesheet" href="https://fonts.googleapis.com/css2?family=Mulish:wght@400;700&display=swap">
<style>
  :root {
    --backdrop: #e4e4e4;
    --paper: #ffffff;
    --brand-green: #2e6a45;
    --foliage-tint: #dfe8e2;
    --foliage-edge: #eef3ef;
    --rule: #8a8a8a;
    --ink: #3d3d3d;
  }
  * { box-sizing: border-box; margin: 0; padding: 0; }
  html, body {
    width: 1200px; height: 1000px; overflow: hidden;
    background: var(--backdrop);
    font-family: "Mulish", sans-serif;
  }
  .letterhead {
    position: absolute;
    left: 252px; top: 50px;
    width: 695px; height: 900px;
    background: var(--paper);
    box-shadow: 0 2px 8px rgba(0,0,0,0.18);
    overflow: hidden;
  }
  .foliage {
    position: absolute;
    border-radius: 40% 60% 50% 50% / 55% 45% 55% 45%;
    background: linear-gradient(160deg, var(--foliage-edge), var(--foliage-tint));
    opacity: 0.75;
  }
  .foliage--top-right   { left: 413px; top: 4px;   width: 177px; height: 336px; }
  .foliage--lower-right { left: 413px; top: 403px; width: 222px; height: 389px; }
  .foliage--lower-left  { left: 0;     top: 276px; width: 283px; height: 559px; }
  .brand {
    position: absolute;
    left: 40px; top: 52px;
    display: flex; align-items: center; gap: 10px;
  }
  .brand__dot {
    width: 16px; height: 16px; border-radius: 50%;
    background: var(--brand-green);
  }
  .brand__name {
    font-size: 26px; font-weight: 700;
    letter-spacing: 1px;
    color: var(--brand-green);
  }
  .contact {
    position: absolute;
    left: 53px; right: 53px; top: 845px;
    border-top: 1px solid var(--rule);
    padding-top: 6px;
    text-align: center;
    font-size: 11px; line-height: 14px;
    color: var(--ink);
  }
</style>
</head>
<body>
  <main class="letterhead">
    <div class="foliage foliage--top-right" role="img" aria-label="Faint foliage decoration"></div>
    <div class="foliage foliage--lower-right" role="img" aria-label="Faint foliage decoration"></div>
    <div class="foliage foliage--lower-left" role="img" aria-label="Faint foliage decoration"></div>

    <header class="brand">
      <span class="brand__dot"></span>
      <span class="brand__name">Terra-Vantage</span>
    </header>

    <footer class="contact">
      <p>1850 Meadowbrook Road Fernhill, NJ 07190 | Ph: (555) 014 -2260 | Fax: (555) 014 - 2291</p>
      <p>service@terra-vantage.example | www.terra-vantage.example</p>
    </footer>
  </main>
</body>
</html>
```